Tech Savy small Business accountant business card design

We need a business card for a new company based in the cloud. We provide tax, business advisory, accounting, information technology solutions and back office functions to small businesses. We offer fixed fee packages with add on services as you need them. By harnessing technology we simplify small business operational processes providing valuable time and information for small business owners to grow their business. In the logo (zulvarine) we want to be able to see zulv and experts. The final design should communicate achieving growth dreams and balance (ie life and $).
Updates
This project has been temporarily placed on hold until I finalize "Tech Savy small Business accountant needs a logo". I invite all designers to submit on this logo project. Once my logo is finalized I will resume this business card contest. Thanks Added Wednesday, March 19, 2014
This project has been temporarily placed on hold until I finalize "Tech Savy small Business accountant logo". I invite all designers to submit on this logo project. Once my logo is finalized I will resume this business card contest. Thanks Added Thursday, March 20, 2014
Target Market(s)
Small Business (Revenue $500,000, more than 3 employees) owners.
Industry/Entity Type
Small Business
Contact Information for Business Card
Marla Pennick (Principal)
Accountant, Tax Agent.
TEL | 0417 583 916
EMAIL | Marla.Pennick@zulvarine.com.au
WEB | www.zulvarine.com.au
Look and feel

```html
<!DOCTYPE html>
<html lang="en">
<head>
<meta charset="utf-8">
<title>zulvarine business card</title>
<link rel="stylesheet" href="https://fonts.googleapis.com/css2?family=Poppins:wght@300;400;600;700&display=swap">
<style>
  :root {
    --stage: #e9e7e3;
    --card-white: #f7f7f7;
    --card-grey: #ececec;
    --brand-blue: #1fb3df;
    --brand-blue-deep: #179fd0;
    --ink-grey: #8b8b8e;
    --ink-soft: #9a9a9c;
    --white: #ffffff;
  }
  * { box-sizing: border-box; margin: 0; padding: 0; }
  html, body { width: 1200px; height: 780px; overflow: hidden; }
  body {
    background: var(--stage);
    font-family: "Poppins", sans-serif;
    position: relative;
  }
  .card {
    position: absolute;
    width: 540px;
    height: 300px;
    border-radius: 3px;
    box-shadow: 0 2px 0 #dcdcdc, 0 4px 0 #d2d2d2, 0 6px 0 #c8c8c8, 0 14px 24px rgba(0,0,0,.18);
    overflow: hidden;
  }
  /* front */
  .card-front { left: 50px; top: 130px; background: var(--card-white); }
  .front-head { position: absolute; left: 0; right: 0; top: 0; height: 124px; padding: 22px 0 0 40px; }
  .wordmark {
    font-weight: 700;
    color: var(--ink-grey);
    letter-spacing: -1px;
    line-height: 1;
  }
  .front-head .wordmark { font-size: 62px; }
  .tagline { color: var(--ink-soft); font-weight: 300; font-size: 19px; margin-top: 6px; letter-spacing: .2px; }
  .contact-band {
    position: absolute; left: 0; right: 0; top: 130px; height: 110px;
    background: linear-gradient(90deg, var(--brand-blue-deep), var(--brand-blue));
    color: var(--white);
    display: flex; align-items: center; padding-left: 40px;
  }
  .person { width: 200px; }
  .person-name { font-size: 24px; font-weight: 400; line-height: 1.1; }
  .person-role { font-size: 13px; font-weight: 300; text-align: right; padding-right: 12px; }
  .person-title { font-size: 14px; font-weight: 300; margin-top: 2px; }
  .band-divider { width: 1.5px; height: 70px; background: var(--white); margin: 0 14px 0 6px; }
  .contact-list { list-style: none; font-size: 13.5px; font-weight: 300; }
  .contact-list li { display: flex; align-items: center; gap: 7px; line-height: 22px; }
  .contact-icon { width: 15px; height: 15px; background: var(--white); border-radius: 2px; flex: none; }
  .front-foot {
    position: absolute; left: 0; right: 0; top: 240px; bottom: 0;
    display: flex; align-items: center; padding-left: 268px;
    color: var(--ink-soft); font-size: 14px; font-weight: 300;
  }
  /* back */
  .card-back {
    left: 610px; top: 360px;
    background: linear-gradient(160deg, var(--card-white), var(--card-grey));
    display: flex; flex-direction: column; align-items: center; justify-content: center;
  }
  .card-back .wordmark { font-size: 70px; }
  .card-back .tagline { font-size: 19px; margin-top: 4px; }
</style>
</head>
<body>
  <section class="card card-front" aria-label="Business card front">
    <div class="front-head">
      <div class="wordmark">zulvarine</div>
      <div class="tagline">Your business and accounting partner</div>
    </div>
    <div class="contact-band">
      <div class="person">
        <div class="person-name">Marla Pennick</div>
        <div class="person-role">(Principal)</div>
        <div class="person-title">Accountant, Tax Agent</div>
      </div>
      <div class="band-divider"></div>
      <ul class="contact-list">
        <li>
          <svg class="contact-icon" viewBox="0 0 16 16" aria-hidden="true"><rect width="16" height="16" rx="2" fill="#fff"/><path d="M5 3.5l1.8 2.2-1 1.2a7 7 0 0 0 3.3 3.3l1.2-1 2.2 1.8-1 1.5C8 12.6 3.4 8 3.5 4.5z" fill="#1fb3df"/></svg>
          0417 583 916
        </li>
        <li>
          <svg class="contact-icon" viewBox="0 0 16 16" aria-hidden="true"><rect width="16" height="16" rx="2" fill="#fff"/><rect x="3" y="4.5" width="10" height="7" fill="none" stroke="#1fb3df" stroke-width="1.2"/><path d="M3 4.5l5 4 5-4" fill="none" stroke="#1fb3df" stroke-width="1.2"/></svg>
          Marla.Pennick@zulvarine.com.au
        </li>
        <li>
          <svg class="contact-icon" viewBox="0 0 16 16" aria-hidden="true"><rect width="16" height="16" rx="2" fill="#fff"/><circle cx="8" cy="8" r="4.8" fill="none" stroke="#1fb3df" stroke-width="1.1"/><ellipse cx="8" cy="8" rx="2" ry="4.8" fill="none" stroke="#1fb3df" stroke-width="1"/><path d="M3.2 8h9.6" stroke="#1fb3df" stroke-width="1"/></svg>
          www.zulvarine.com.au
        </li>
      </ul>
    </div>
    <div class="front-foot">Carrowbay NSW Australia</div>
  </section>

  <section class="card card-back" aria-label="Business card back">
    <div class="wordmark">zulvarine</div>
    <div class="tagline">Your business and accounting partner</div>
  </section>
</body>
</html>
```